HLD business cards Dr. Martin Voss

I need a business card designed for our dental office. We are a "general dental" practice.
Looking for a clean, professional but not too fancy design with our logo and contact information required.
front of card is information/standard business card, backside is appt reminder with lines for date and time of appt
doctors name: Dr. Martin Voss DMD
office name: Voss Family Dental
address: 4827 N Birchwell Ave Linden Harbor, FL 33412
phone: 954-555-0173
Contact Information for Business Card
Office name, Doctor name, address, phone number...etc
- White/off white base color, blue and or black lettering

```html
<!DOCTYPE html>
<html lang="en">
<head>
<meta charset="utf-8">
<title>Voss Family Dental – Business Cards</title>
<link href="https://fonts.googleapis.com/css2?family=Crimson+Pro:ital,wght@0,400;0,600;0,700;1,400&display=swap" rel="stylesheet">
<style>
  :root {
    --backdrop: #464648;
    --card: #ffffff;
    --ink: #111111;
    --rule: #3a4550;
  }
  * { margin: 0; padding: 0; box-sizing: border-box; }
  html, body { width: 1200px; height: 1200px; overflow: hidden; }
  body {
    background: var(--backdrop);
    position: relative;
    font-family: "Crimson Pro", Georgia, serif;
    color: var(--ink);
  }
  .card {
    position: absolute;
    left: 233px;
    width: 735px;
    height: 448px;
    background: var(--card);
    border-radius: 34px;
  }
  .card--front { top: 129px; }
  .card--back { top: 623px; }

  /* front */
  .brand-mark {
    position: absolute;
    left: 504px; top: 88px;
    width: 80px; height: 80px;
    border: 9px solid var(--ink);
    border-radius: 50%;
  }
  .brand {
    position: absolute;
    left: 400px; top: 200px;
    width: 290px;
    text-align: center;
    font-weight: 700;
    font-size: 34px;
    line-height: 36px;
    letter-spacing: 1px;
  }
  .brand-sub {
    display: block;
    font-size: 18px;
    line-height: 22px;
    letter-spacing: 9px;
  }
  .doctor {
    position: absolute;
    left: 63px; top: 235px;
    font-weight: 700;
    font-size: 29px;
    line-height: 36px;
  }
  .contact, .address {
    position: absolute;
    top: 294px;
    font-weight: 700;
    line-height: 23px;
  }
  .contact { left: 62px; font-size: 19.5px; }
  .address { left: 413px; font-size: 21px; }
  .divider {
    position: absolute;
    left: 386px; top: 294px;
    width: 5px; height: 44px;
    background: var(--rule);
  }

  /* back */
  .appt-title {
    position: absolute;
    left: 0; right: 0; top: 48px;
    text-align: center;
    font-style: italic;
    font-weight: 400;
    font-size: 34px;
    line-height: 40px;
  }
  .slots { position: absolute; left: 61px; top: 125px; width: 330px; }
  .slot { height: 77px; }
  .days {
    display: flex;
    justify-content: space-between;
    font-size: 15px;
    height: 22px;
    align-items: center;
  }
  .day::before {
    content: "";
    display: inline-block;
    width: 10px; height: 10px;
    border: 1.4px solid var(--ink);
    margin-right: 3px;
    vertical-align: -1px;
  }
  .when {
    display: flex;
    align-items: flex-start;
    font-size: 12px;
    line-height: 14px;
    margin-top: 9px;
    margin-left: 3px;
  }
  .blank { border-bottom: 1px solid var(--ink); height: 13px; }
  .blank--date { width: 178px; }
  .blank--time { width: 68px; }
  .label-time { margin-left: 4px; }
  .meridiem { font-size: 11px; line-height: 13px; margin-left: 6px; margin-top: -3px; }
  .brand-large {
    position: absolute;
    left: 450px; top: 160px;
    width: 250px;
    text-align: center;
    font-weight: 700;
    font-size: 40px;
    line-height: 46px;
  }
  .notice {
    position: absolute;
    left: 0; right: 0; top: 372px;
    text-align: center;
    font-style: italic;
    font-size: 20px;
    line-height: 26px;
  }
</style>
</head>
<body>
  <section class="card card--front">
    <div class="brand-mark"></div>
    <div class="brand">VOSS FAMILY<span class="brand-sub">DENTAL</span></div>
    <h1 class="doctor">Dr. Martin Voss, DMD</h1>
    <p class="contact">954-555-0173<br>martin@vossfamilydental.com</p>
    <div class="divider"></div>
    <p class="address">4827 N Birchwell Ave<br>Linden Harbor, FL 33412</p>
  </section>

  <section class="card card--back">
    <h2 class="appt-title">Your next Appointment is:</h2>
    <div class="slots">
      <div class="slot">
        <div class="days"><span class="day">Mon.</span><span class="day">Tues.</span><span class="day">Wed.</span><span class="day">Thurs.</span><span class="day">Fri.</span><span class="day">Sat.</span></div>
        <div class="when"><span>Date</span><span class="blank blank--date"></span><span class="label-time">Time</span><span class="blank blank--time"></span><span class="meridiem">A.M.<br>P.M.</span></div>
      </div>
      <div class="slot">
        <div class="days"><span class="day">Mon.</span><span class="day">Tues.</span><span class="day">Wed.</span><span class="day">Thurs.</span><span class="day">Fri.</span><span class="day">Sat.</span></div>
        <div class="when"><span>Date</span><span class="blank blank--date"></span><span class="label-time">Time</span><span class="blank blank--time"></span><span class="meridiem">A.M.<br>P.M.</span></div>
      </div>
      <div class="slot">
        <div class="days"><span class="day">Mon.</span><span class="day">Tues.</span><span class="day">Wed.</span><span class="day">Thurs.</span><span class="day">Fri.</span><span class="day">Sat.</span></div>
        <div class="when"><span>Date</span><span class="blank blank--date"></span><span class="label-time">Time</span><span class="blank blank--time"></span><span class="meridiem">A.M.<br>P.M.</span></div>
      </div>
    </div>
    <div class="brand-large">Voss<br>Family<br>Dental</div>
    <p class="notice">If unable to keep appointment, kindly give 24 hour notice.</p>
  </section>
</body>
</html>
```